Business card design for crowd sourced review site.

I need a business card magnet design for an online, crowd-sourced, restaurant review site strictly for Kosher restaurants.
It is similar to WanderNotes but catering to a very particular crowd.
The markets it will be distributed in are flooded with business card fridge magnets so this needs to be eye-catching and unique. The Business name is PlateRanker
The website isnt finished but you can see the basic setup here
http://dining.brevtalo.com/

The second image i included is another logo design I liked and was thinking about using and decided I will probably also make a SECOND custom cut business card in the shape of that icon. Bonus if you can throw that in also.

Target Market(s)

Jewish consumers aged 20-35

Industry/Entity Type

Business

Contact Information for Business Card

see description.
Design should not be too crowded and should in eye-catching. Will mainly be used as fridge magnets.

Requirements
Must have
• Website address. logo.
Nice to have
• tagline. (The Definitive guide to kosher dining for the Kosher consumer)
• Im not a professional but I personally think the color blue goes along with this concept. ill leave it to you to decide.
Should not have
• any religious symbols.

```html
<!DOCTYPE html>
<html lang="en">
<head>
<meta charset="utf-8">
<title>PlateRanker business cards</title>
<link rel="stylesheet" href="https://fonts.googleapis.com/css2?family=Source+Sans+3:ital,wght@0,400;0,600;1,400&display=swap">
<style>
  :root {
    --backdrop: #5b4a3d;
    --card: #000000;
    --accent: #d8302a;
    --text: #e6e6e6;
    --muted: #cfcfcf;
    --shadow: rgba(0, 0, 0, 0.45);
  }
  * { margin: 0; padding: 0; box-sizing: border-box; }
  html, body {
    width: 1200px;
    height: 987px;
    overflow: hidden;
    background: var(--backdrop);
    font-family: "Source Sans 3", "Myriad Pro", sans-serif;
  }
  .canvas { position: relative; width: 1200px; height: 987px; }
  .card {
    position: absolute;
    left: 293px;
    width: 615px;
    height: 351px;
    background: var(--card);
    box-shadow: 0 3px 8px var(--shadow);
    overflow: hidden;
  }
  .card--front { top: 130px; }
  .card--back { top: 505px; }

  .accent-bar {
    position: absolute;
    left: 0; top: 71px;
    width: 13px; height: 40px;
    background: var(--accent);
  }
  .contact { position: absolute; left: 48px; top: 66px; color: var(--text); }
  .contact__name {
    font-size: 23px; font-weight: 600; color: var(--accent);
    letter-spacing: 0.3px; line-height: 28px;
  }
  .contact__role { font-size: 17px; line-height: 22px; }
  .contact__address { margin-top: 11px; font-size: 16px; line-height: 21px; }
  .contact__list { list-style: none; margin-top: 8px; }
  .contact__item {
    display: flex; align-items: center;
    font-size: 16px; line-height: 23.5px;
  }
  .contact__icon { width: 14px; height: 14px; margin-right: 12px; fill: var(--accent); }

  .brand {
    position: absolute;
    font-weight: 600;
    color: #ffffff;
    display: flex; align-items: center;
  }
  .brand__dot {
    width: 16px; height: 16px; border-radius: 50%;
    background: var(--accent); margin-right: 10px;
  }
  .brand--front { left: 340px; top: 155px; font-size: 30px; }
  .brand--back {
    left: 0; right: 0; top: 118px;
    justify-content: center; font-size: 44px;
  }
  .brand--back .brand__dot { width: 24px; height: 24px; margin-right: 14px; }

  .tagline {
    position: absolute; left: 0; right: 0; top: 291px;
    text-align: center; font-style: italic;
    font-size: 17px; color: var(--muted);
  }
</style>
</head>
<body>
<main class="canvas">
  <section class="card card--front">
    <span class="accent-bar"></span>
    <div class="contact">
      <p class="contact__name">DANA LEVIN</p>
      <p class="contact__role">CEO/Founder</p>
      <p class="contact__address">1420 Maplewood Court<br>Fairbrook, Oregon 97512</p>
      <ul class="contact__list">
        <li class="contact__item">
          <svg class="contact__icon" viewBox="0 0 14 14"><path d="M3 1l2.5 3-1.3 1.6c.8 1.7 2.2 3.1 3.9 3.9L9.7 8.2 13 10.6 11.6 13C6 12.6 1.4 8 1 2.4z"/></svg>
          541 203 7786
        </li>
        <li class="contact__item">
          <svg class="contact__icon" viewBox="0 0 14 14"><path d="M4 0h6a1 1 0 0 1 1 1v12a1 1 0 0 1-1 1H4a1 1 0 0 1-1-1V1a1 1 0 0 1 1-1zm.5 1.5v9.5h5V1.5zM7 11.7a.8.8 0 1 0 0 1.6.8.8 0 0 0 0-1.6z"/></svg>
          541 917 4420
        </li>
        <li class="contact__item">
          <svg class="contact__icon" viewBox="0 0 14 14"><path d="M3.5 1h7v3.5h-7zM1 5h12v6h-2v-2H3v2H1zM3.5 9.5h7V13h-7z"/></svg>
          541 203 7790
        </li>
        <li class="contact__item">
          <svg class="contact__icon" viewBox="0 0 14 14"><path d="M0 3h14v1L7 8.3 0 4zM0 5.3l7 4.3 7-4.3V11H0z"/></svg>
          dana@plateranker.com
        </li>
        <li class="contact__item">
          <svg class="contact__icon" viewBox="0 0 14 14"><path d="M7 0a7 7 0 1 0 0 14A7 7 0 0 0 7 0zm-1 2.2C4.5 3.5 5 5 6.5 5.5 8 6 7.3 7.6 6 8.3c-1 .5-.7 2-.2 3.4A5 5 0 0 1 6 2.2zm3 9c.3-1 1-2 2-2.6A5 5 0 0 1 9 11.2z"/></svg>
          www.plateranker.com
        </li>
      </ul>
    </div>
    <div class="brand brand--front"><span class="brand__dot"></span>PlateRanker</div>
  </section>

  <section class="card card--back">
    <div class="brand brand--back"><span class="brand__dot"></span>PlateRanker</div>
    <p class="tagline">The Definitive guide to kosher dining for the Kosher consumer</p>
  </section>
</main>
</body>
</html>
```